Corporate Design für Vermietung von Geschäftslokalen
Zielgruppe
Vermietung von Geschäftslokalen, Büros und Lagerhallen, Bauträger
Betrieb von Tankstellen
Design sollte vor allem auf die Vermietung von Gewerbeobjekten abzielen.
Logo sollte immobilienlastig sein.
Aufgabenstellung
Moderne Optik

```html
<!DOCTYPE html>
<html lang="de">
<head>
<meta charset="utf-8">
<title>K. Wendler GmbH – Corporate Design</title>
<link href="https://fonts.googleapis.com/css2?family=Montserrat:wght@600&family=Open+Sans:wght@400;600&display=swap" rel="stylesheet">
<style>
  :root{
    --page:#f3f3f3;
    --white:#ffffff;
    --band-dark-a:#353230;
    --band-dark-b:#615d5a;
    --block-grey:#a9a9a9;
    --logo-grey:#8c8c8c;
    --logo-dark:#4a4745;
    --logo-silver:#e6e6e6;
    --text:#555555;
    --text-soft:#8a8a8a;
    --line:#d6d6d6;
    --shadow:0 2px 8px rgba(0,0,0,.22);
  }
  *{box-sizing:border-box;margin:0;padding:0}
  html,body{width:1200px;height:556px;overflow:hidden}
  body{background:var(--page);font-family:"Open Sans",Arial,sans-serif;color:var(--text);position:relative}

  .band{position:absolute;left:0;width:1200px}
  .band--white{top:113px;height:169px;background:var(--white)}
  .band--dark{top:282px;height:169px;background:linear-gradient(180deg,var(--band-dark-a),var(--band-dark-b))}
  .block{position:absolute;top:451px;height:86px}
  .block--grey{left:0;width:206px;background:var(--block-grey)}
  .block--white{left:206px;width:211px;background:var(--white)}

  .wordmark{position:absolute;display:flex;align-items:center;gap:.35em;font-family:"Montserrat",Arial,sans-serif;font-weight:600;white-space:nowrap;letter-spacing:.01em;line-height:1}
  .wordmark__square{width:.55em;height:.55em;background:currentColor;flex:none}
  .wordmark--grey{color:var(--logo-grey)}
  .wordmark--silver{color:var(--logo-silver)}
  .wordmark--dark{color:var(--logo-dark)}
  .wordmark--white{color:var(--white)}

  .sheet{position:absolute;background:var(--white);box-shadow:var(--shadow)}

  .letter{left:419px;top:33px;width:338px;height:482px}
  .letter__address{position:absolute;left:37px;top:97px;font-size:4.6px}
  .letter__body{position:absolute;left:37px;top:110px;width:286px;font-size:4.1px;line-height:5.6px;text-align:justify}
  .letter__body p{margin-bottom:5.6px}
  .letter__body p.gap{margin-bottom:16px}
  .letter__watermark{position:absolute;left:77px;top:326px;font-family:"Montserrat",Arial,sans-serif;font-weight:600;font-size:18px;color:#ececec;white-space:nowrap}
  .letter__signature{position:absolute;left:226px;top:312px;width:90px;height:44px;border-radius:6px;background:linear-gradient(135deg,rgba(70,80,130,.18),rgba(70,80,130,.06))}
  .letter__footer{position:absolute;left:37px;right:28px;top:449px;border-top:1px solid var(--line);padding-top:5px;display:flex;gap:36px;font-size:3.8px;line-height:5px;color:var(--text-soft)}
  .letter__footer strong{color:var(--text);font-weight:600}

  .card{width:170px;height:109px;top:35px}
  .card--dark{left:790px;background:linear-gradient(180deg,#3b3836,#6a6663)}
  .card--light{left:996px}
  .card__person{position:absolute;left:26px;top:58px;font-size:6.5px;line-height:7px}
  .card__person strong{font-weight:600;color:#333}
  .card__contacts{position:absolute;left:98px;top:58px;list-style:none;font-size:4px;line-height:5.6px;color:var(--text-soft)}
  .card__contacts li{display:flex;align-items:flex-start;gap:4px}
  .card__contacts svg{flex:none;margin-top:.5px}

  .envelope{left:786px;width:381px}
  .envelope--front{top:162px;height:167px}
  .envelope__window{position:absolute;left:22px;top:82px;width:153px;height:56px;border-radius:9px;background:var(--white);box-shadow:inset 0 0 3px rgba(0,0,0,.18)}
  .envelope--back{top:340px;height:171px;overflow:hidden}
  .envelope__flap{position:absolute;left:0;top:0}
</style>
</head>
<body>
  <div class="band band--white"></div>
  <div class="band band--dark"></div>
  <div class="block block--grey"></div>
  <div class="block block--white"></div>

  <!-- logo presentation -->
  <div class="wordmark wordmark--grey" style="left:60px;top:184px;font-size:27px"><span class="wordmark__square"></span>K. WENDLER GmbH</div>
  <div class="wordmark wordmark--silver" style="left:60px;top:352px;font-size:27px"><span class="wordmark__square"></span>K. WENDLER GmbH</div>
  <div class="wordmark wordmark--white" style="left:32px;top:486px;font-size:13.5px"><span class="wordmark__square"></span>K. WENDLER GmbH</div>
  <div class="wordmark wordmark--dark" style="left:240px;top:486px;font-size:13.5px"><span class="wordmark__square"></span>K. WENDLER GmbH</div>

  <!-- letterhead -->
  <article class="sheet letter">
    <div class="wordmark wordmark--dark" style="left:196px;top:57px;font-size:10px"><span class="wordmark__square"></span>K. WENDLER GmbH</div>
    <p class="letter__address">Your Company · Your adress 12 · 34567 Your town</p>
    <div class="letter__watermark">K. WENDLER GmbH</div>
    <div class="letter__body">
      <p>Gewerbeflächen in zentraler Lage bieten Ihrem Unternehmen beste Voraussetzungen für Wachstum. Wir vermieten Büros, Geschäftslokale und Lagerhallen in unterschiedlichen Größen und begleiten Sie von der ersten Besichtigung bis zur Übergabe. Unsere Objekte sind modern ausgestattet, gut erreichbar und flexibel nutzbar. Gerne erstellen wir Ihnen ein individuelles Angebot, das genau auf Ihre Anforderungen abgestimmt ist und Ihnen langfristige Planungssicherheit gibt.</p>
      <p class="gap">Als erfahrener Bauträger planen und errichten wir Gewerbeobjekte nach Ihren Wünschen. Auch der Betrieb unserer Tankstellen gehört seit vielen Jahren zu unseren Aufgaben. Sprechen Sie uns an, wir beraten Sie gerne persönlich.</p>
      <p>Gewerbeflächen in zentraler Lage bieten Ihrem Unternehmen beste Voraussetzungen für Wachstum. Wir vermieten Büros, Geschäftslokale und Lagerhallen in unterschiedlichen Größen und begleiten Sie von der ersten Besichtigung bis zur Übergabe. Unsere Objekte sind modern ausgestattet, gut erreichbar und flexibel nutzbar. Gerne erstellen wir Ihnen ein individuelles Angebot, das genau auf Ihre Anforderungen abgestimmt ist und Ihnen langfristige Planungssicherheit gibt.</p>
      <p>Als erfahrener Bauträger planen und errichten wir Gewerbeobjekte nach Ihren Wünschen. Auch der Betrieb unserer Tankstellen gehört seit vielen Jahren zu unseren Aufgaben. Sprechen Sie uns an, wir beraten Sie gerne persönlich.</p>
    </div>
    <div class="letter__signature" role="img" aria-label="Handschriftliche Unterschrift"></div>
    <footer class="letter__footer">
      <div><strong>Your Company</strong><br>CEO Your Name<br>Your adress 12<br>34567 Your Town</div>
      <div>1234 - 56 78 90 00<br>1234 - 56 78 90 00<br>your.name@yourweb.de<br>www.yourweb.de</div>
      <div>Bankverbindung<br>Iban: DE0123456789012345678<br>BIC:<br>UST-ID: 000000000000000</div>
    </footer>
  </article>

  <!-- business cards -->
  <div class="sheet card card--dark">
    <div class="wordmark wordmark--silver" style="left:26px;top:49px;font-size:11px"><span class="wordmark__square"></span>K. WENDLER GmbH</div>
  </div>
  <div class="sheet card card--light">
    <div class="wordmark wordmark--grey" style="left:34px;top:23px;font-size:9.5px"><span class="wordmark__square"></span>K. WENDLER GmbH</div>
    <p class="card__person"><strong>Your Name</strong><br>CEO</p>
    <ul class="card__contacts">
      <li><svg width="4" height="5" viewBox="0 0 4 5"><path d="M2 5C1 3.6 0 2.7 0 1.8A2 2 0 0 1 4 1.8C4 2.7 3 3.6 2 5Z" fill="#9a9a9a"/></svg><span>Your Adress 12, 34567<br>Your Town</span></li>
      <li><svg width="4" height="4" viewBox="0 0 4 4"><path d="M.4 .3 1.3 0 1.8 1.2 1.2 1.6A2.6 2.6 0 0 0 2.4 2.8L2.8 2.2 4 2.7 3.7 3.6C2 3.9 .1 2 .4 .3Z" fill="#9a9a9a"/></svg><span>+00 123 456 789</span></li>
      <li><svg width="4" height="5" viewBox="0 0 4 5"><rect x=".6" y="0" width="2.8" height="5" rx=".5" fill="#9a9a9a"/></svg><span>+00 123 456 789</span></li>
      <li><svg width="5" height="4" viewBox="0 0 5 4"><rect width="5" height="3.6" rx=".4" fill="#9a9a9a"/></svg><span>your.name@your-web.de</span></li>
      <li><svg width="4" height="4" viewBox="0 0 4 4"><circle cx="2" cy="2" r="1.8" fill="none" stroke="#9a9a9a" stroke-width=".6"/></svg><span>www.your-web.de</span></li>
    </ul>
  </div>

  <!-- envelopes -->
  <div class="sheet envelope envelope--front">
    <div class="envelope__window"></div>
    <div class="wordmark wordmark--grey" style="left:258px;top:136px;font-size:8.5px"><span class="wordmark__square"></span>K. WENDLER GmbH</div>
  </div>
  <div class="sheet envelope envelope--back">
    <svg class="envelope__flap" width="381" height="171" viewBox="0 0 381 171">
      <defs>
        <linearGradient id="flapShade" x1="0" y1="0" x2="0" y2="1">
          <stop offset="0" stop-color="#3b3836"/>
          <stop offset="1" stop-color="#5e5a57"/>
        </linearGradient>
      </defs>
      <path d="M0 0H381V2L362 40Q358 46 350 46H31Q23 46 19 40L0 2Z" fill="url(#flapShade)"/>
    </svg>
    <div class="wordmark wordmark--silver" style="left:150px;top:19px;font-size:8px"><span class="wordmark__square"></span>K. WENDLER GmbH</div>
  </div>
</body>
</html>
```